Long Established Local Fencing (not swords) Business needs fresh Business Cards

We need fresh double sided business cards for our Fencing Construction business, we are looking for something with our new logo design added, and maybe a photo background ?
We recently had cards made from Cardlyne and we were horrified with what we got back, the quality was terrible, so am looking for high quality format for good printing company to make.
We install Steelmora, Timber paling, Aluminium Slat Screening, Picket (timber and aluminium) and most other fencing installations.
Our website is brankelrails.com.au should you like to learn a bit more.
We do have logo in other formats if required.
We have been in business for over 35 years and we have used this as a "motto" it is on our signage

Industry/Entity Type

Construction

Contact Information for Business Card

Open to ideas, we need 3 x different cards, one generic with no name and 2 x others each with 1 of our bosses name on each, I will put into upload files.

Colors
ec1f27
000000
606060
f5f5f5

Requirements
Must have
• Company Name and Logo
• Address
• Contact details, phone, website, email etc
• Small space to write notes when leaving card at residence
Nice to have
• Our motto "Servicing the Peninsula for over 35 years"

```html
<!DOCTYPE html>
<html lang="en">
<head>
<meta charset="utf-8">
<title>Brankel Rails – Business Cards</title>
<link href="https://fonts.googleapis.com/css2?family=Lato:wght@400;900&display=swap" rel="stylesheet">
<style>
  :root {
    --red: #ec1f27;
    --black: #000000;
    --grey: #606060;
    --white: #f5f5f5;
    --card: #1f1f20;
    --card-back: #161617;
    --backdrop: #2a2a2b;
  }
  * { box-sizing: border-box; margin: 0; padding: 0; }
  html, body {
    width: 1200px; height: 900px; overflow: hidden;
    background: var(--backdrop);
    font-family: "Lato", Arial, sans-serif;
  }
  .canvas { position: relative; width: 1200px; height: 900px; }
  .card {
    position: absolute; left: 240px; width: 720px; height: 412px;
    box-shadow: 0 10px 30px rgba(0,0,0,.45);
  }
  .card--back { top: 28px; background: var(--card-back); overflow: hidden; }
  .card--front { top: 460px; background: var(--card); }

  .back-pattern {
    position: absolute; inset: 0;
    background: radial-gradient(ellipse at 50% 50%, #2c2c2e 0%, #1c1c1d 55%, #141415 100%);
  }
  .back-wordmark {
    position: absolute; inset: 0;
    display: flex; align-items: center; justify-content: center;
  }

  .wordmark {
    font-weight: 900; color: var(--white);
    text-transform: uppercase; letter-spacing: 3px; line-height: 1;
    display: flex; align-items: center; gap: 14px;
  }
  .wordmark__dot {
    width: 20px; height: 20px; border-radius: 50%; background: var(--red); flex: none;
  }
  .back-wordmark .wordmark { font-size: 54px; }

  .front-brand {
    position: absolute; left: 0; top: 0; width: 330px; height: 100%;
    display: flex; align-items: center; justify-content: center;
  }
  .front-brand .wordmark { font-size: 32px; letter-spacing: 2px; }
  .divider {
    position: absolute; left: 330px; top: 92px; width: 2px; height: 228px;
    background: var(--white);
  }
  .contact {
    position: absolute; left: 372px; top: 98px; color: var(--white);
  }
  .contact__name {
    color: var(--red); font-size: 32px; font-weight: 400;
    text-transform: uppercase; letter-spacing: 1px; line-height: 1;
  }
  .contact__role { font-size: 18px; margin-top: 6px; }
  .contact__address { font-size: 19px; line-height: 1.3; margin-top: 18px; }
  .contact__list { list-style: none; margin-top: 16px; }
  .contact__item {
    display: flex; align-items: center; gap: 12px;
    font-size: 19px; line-height: 1.55;
  }
  .contact__icon { width: 13px; height: 13px; flex: none; }
  .accent { color: var(--red); }
</style>
</head>
<body>
<main class="canvas">
  <section class="card card--back">
    <div class="back-pattern" role="img" aria-label="Repeating faint pattern of the company emblem in dark grey and red"></div>
    <div class="back-wordmark">
      <div class="wordmark">Brankel Rails</div>
    </div>
  </section>

  <section class="card card--front">
    <div class="front-brand">
      <div class="wordmark"><span class="wordmark__dot"></span>Brankel Rails</div>
    </div>
    <div class="divider"></div>
    <div class="contact">
      <h1 class="contact__name">Dorian Keats</h1>
      <p class="contact__role">Director</p>
      <p class="contact__address">42 Tarlow Street<br>Brankel Nsw 2261</p>
      <ul class="contact__list">
        <li class="contact__item">
          <svg class="contact__icon" viewBox="0 0 16 16"><path fill="#ec1f27" d="M3.6 1 6 3.6 4.8 5.4c.8 2.2 3.6 5 5.8 5.8l1.8-1.2L15 12.4 13.3 15C6.8 15 1 9.2 1 2.7z"/></svg>
          02 4100 5827
        </li>
        <li class="contact__item">
          <svg class="contact__icon" viewBox="0 0 16 16"><rect x="1" y="3" width="14" height="10" fill="none" stroke="#ec1f27" stroke-width="1.6"/><path d="M1 3l7 6 7-6" fill="none" stroke="#ec1f27" stroke-width="1.6"/></svg>
          brankelrails@mailhub.com
        </li>
        <li class="contact__item">
          <svg class="contact__icon" viewBox="0 0 16 16"><g fill="none" stroke="#ec1f27" stroke-width="1.4"><circle cx="8" cy="8" r="6.5"/><ellipse cx="8" cy="8" rx="3" ry="6.5"/><path d="M1.5 8h13"/></g></svg>
          <span>www.<span class="accent">brankelrails</span>.com.au</span>
        </li>
      </ul>
    </div>
  </section>
</main>
</body>
</html>
```